Web Concept Design - modernize website

Looking to modernize our current website. http :// hvmcoldbrook . com

Color Scheme: Use uploaded palette. (Black, Silver, Dark Purple, Greyish Blue)

The website needs to have a patient-friendly, community-friendly feel to it. While still being a professional medical website. We don't want it to have a cold, clinical feel.

Information on home page needs to be split into their own separate pages with designs for each.

Home Page:
Harborview Walk-In & Family Care is a family practice and urgent care clinic dedicated to providing high quality, compassionate health care, to patients of all ages.
Hours of operation:
Monday-Friday 9am-6:30pm
Saturday: CLOSED
Sunday: CLOSED
Primary Care visits will be by appointment only.
We will accept our last new patient at 6:00p and our last established patient at 6:30p.
We will no longer be doing DOT Physicals.

At bottom of home page:

Harborview Walk-In & Family Care understands that information about your health is private and we know how important it is to keep your medical information protected. We follow all HIPAA guidelines to protect the privacy of your medical records. The privacy act below explains our privacy practices and how we may use and disclose your medical information. If you would like for Harborview Walk-In & Family Care to release any or all of your medical information to others, you can make the request by signing a release and bring it with you at your next visit. If you would like to contact someone about the privacy and/or use of your medical information, you may contact us at 205-381-7260.

Click here for HIPAA document.

Click here for Medical Release form.

---------------

Services Page:
We provide family and urgent care for patients of all ages.

-Annual physicals
-Pre-employment drug screening
-Women's care including pap smears
-Screening and treatment for diabetes, hypertension and cholesterol
-All minor trauma such as abscesses, lacerations, burns and fractures
-Minor skin complaints
-Onsite LAB/XRAY/EKG
-Weight loss
-Adult and Pediatric Vaccinations
-Osteopathic manual medicine
-Medical pain management

-----

Payment & Insurance Page:
We now have online bill pay for patient balances. Please visit https://secure.paytrellixmed.example/hvmc382pay to pay your bill today!

We currently accept all forms of insurance with the exception of Medicaid. Please bring a copy of your insurance card and photo ID upon visit. We are also a Servimed prime provider. We do accept self-pay for patients who do not have insurance.

----

Meet Our Providers Page:

Dr. Daniel (Dan) Whitcomb, DO
Family Practice Physician

Professional Experience
April 4, 2010 to Present Harborview Walk-In & Family Care Owner
12 years of Emergency Medicine experience
6/1994 - 7/1997 KLT Birmingham, AL
Family Medicine Residency
10/1997 to Present Board Certified in Family Medicine
Recertified 2004
Education
9/1990 to 5/1994 Eastbrook College of Osteopathic Medicine
Old Westbury, New York
Degree: Doctor of Osteopathic Medicine
9/1985 to 5/1989 Caldwell-Ridgemont College
Birmingham, Alabama
Degree: Bachelor of Science
Membership
National Guild of Family Practitioners
Physicians Council of the State of Alabama

----

Navigation Bar should have links for all the above pages + NEW PATIENTS + Access Your Medical Records (feel free to be creative with how you design this). We don't want the navigation bar to be too crowded.

Target Market(s)

Medical Patients

Number of Pages Required

5+ page

Colors

Designer to choose colors to be used in the design.

Requirements
Must have
• Designs for all pages
• Keep it professional
Nice to have
• Be creative!
Should not have
• No cold clinical, medical websites

```html
<!DOCTYPE html>
<html lang="en">
<head>
<meta charset="utf-8">
<title>Harborview Walk-In &amp; Family Care</title>
<link rel="stylesheet" href="https://fonts.googleapis.com/css2?family=Open+Sans:wght@300;400;600;700;800&display=swap">
<style>
:root{
  --navy:#3d3f52;
  --tan:#8b8271;
  --ink:#3a3c4d;
  --text:#4a4a4a;
  --light:#efefef;
  --slate:#6b6b6b;
  --rule:#d9d9d9;
  --white:#ffffff;
  --footer-text:#d7d8e0;
}
*{box-sizing:border-box;margin:0;padding:0}
html,body{width:1007px;height:1200px;overflow:hidden;background:var(--white)}
body{font-family:"Open Sans",Arial,sans-serif;color:var(--text);position:relative}
a{text-decoration:none}

.site-header{position:absolute;left:0;top:0;width:1007px;height:50px;background:var(--navy)}
.brand{position:absolute;left:178px;top:8px;width:150px;color:var(--white);font-size:14px;line-height:17px;font-weight:400}
.main-nav{position:absolute;top:17px;left:388px;display:flex;gap:17px}
.main-nav a{white-space:nowrap;color:var(--white);font-size:8px;font-weight:700;line-height:11px}
.main-nav a.active{border-bottom:1px solid var(--white);padding-bottom:3px}
.nav-cta{position:absolute;left:710px;top:0;width:120px;height:50px;background:var(--tan);color:var(--white);text-align:center;padding-top:9px;white-space:nowrap}
.nav-cta strong{display:block;font-size:13px;font-weight:700;line-height:15px}
.nav-cta span{display:block;font-size:6.3px;font-weight:400;line-height:10px}

.hero{position:absolute;left:0;top:50px;width:1007px;height:332px;overflow:hidden}
.hero-photo{position:absolute;inset:0;background:linear-gradient(100deg,#3b3e45 0%,#5f6670 12%,#2f6fb4 28%,#8ea4b8 45%,#d9dde2 60%,#e9ebee 80%,#c9ccd0 100%)}
.hero-photo::after{content:"";position:absolute;left:0;right:0;bottom:0;height:48px;background:linear-gradient(180deg,#4a4440,#2e2a28)}
.hero-title{position:absolute;top:95px;width:100%;text-align:center;color:var(--white);font-size:56px;line-height:76px;font-weight:800;text-shadow:0 2px 6px rgba(0,0,0,.35)}
.hero-sub{position:absolute;top:166px;width:100%;text-align:center;color:var(--white);font-size:16px;line-height:22px;font-weight:700;letter-spacing:2.5px;text-shadow:0 1px 4px rgba(0,0,0,.35)}
.hero-btn{position:absolute;left:403px;top:209px;width:202px;height:55px;background:var(--tan);color:var(--white);text-align:center;padding-top:10px;white-space:nowrap}
.hero-btn strong{display:block;font-size:13px;font-weight:700;letter-spacing:.5px}
.hero-btn span{display:block;font-size:10.5px;font-weight:400;letter-spacing:.3px;margin-top:3px}

.section-title{position:absolute;top:415px;width:100%;text-align:center;color:var(--ink);font-size:16px;font-weight:800;letter-spacing:3px}

.about{position:absolute;left:169px;top:506px;width:330px}
.intro{color:var(--text);font-size:15px;font-weight:300;line-height:25px}
.hours-title{margin-top:16px;color:var(--ink);font-size:16px;line-height:22px;font-weight:800;letter-spacing:.3px}
.hours{margin-top:9px;width:177px;list-style:none}
.hours li{font-size:11px;height:24px;line-height:22px;padding-left:2px;border-bottom:1px solid var(--rule)}
.hours li:last-child{border-bottom:none}

.photo{position:absolute}
.photo.framed{border:3px solid var(--navy)}
.p1{left:629px;top:490px;width:57px;height:57px;background:linear-gradient(135deg,#d8cfa8,#9aa3b3)}
.p2{left:697px;top:516px;width:172px;height:118px;background:linear-gradient(135deg,#c9c6a4,#e4e2d8 50%,#6a4a34)}
.p3{left:504px;top:558px;width:172px;height:116px;background:linear-gradient(180deg,#b7a792,#6f7390 55%,#3e4560)}
.p4{left:612px;top:662px;width:102px;height:100px;background:linear-gradient(135deg,#e6e6e6,#7a86a0 60%,#2d3550)}
.p5{left:744px;top:661px;width:58px;height:59px;background:linear-gradient(135deg,#8a5a3e,#c9b49a)}
.chip{position:absolute;left:569px;top:695px;width:25px;height:25px;background:var(--rule)}

.notice{position:absolute;top:806px;height:106px}
.notice-a{left:176px;width:220px;background:var(--tan);color:var(--white);padding:20px 0 0 31px}
.notice-a h3{font-size:27px;font-weight:300;line-height:30px}
.notice-a p{font-size:10px;font-weight:700;margin-top:2px}
.notice-b{left:396px;width:216px;background:var(--light);color:var(--text);padding:27px 0 0 23px;font-size:11.5px;line-height:17px}
.notice-c{left:612px;width:220px;background:var(--slate);color:var(--white);padding:27px 0 0 30px;font-size:14px;font-weight:300;line-height:21px}
.notice-c span{font-size:12px}

.privacy{position:absolute;left:176px;top:931px;width:660px;font-size:10px;line-height:17.5px;color:var(--text)}
.doc-links{position:absolute;left:176px;top:1033px;list-style:none}
.doc-links li{font-size:10px;height:20px;display:flex;align-items:center}
.doc-links svg{margin-right:8px}
.doc-links a{color:var(--text);text-decoration:underline}

.site-footer{position:absolute;left:0;top:1116px;width:1007px;height:84px;background:var(--navy);color:var(--footer-text)}
.footer-brand{position:absolute;left:178px;top:18px;width:140px;color:var(--white);font-size:12px;line-height:15px}
.footer-col{position:absolute;top:18px;font-size:9px;line-height:14px;list-style:none;white-space:nowrap}
.footer-col a{color:var(--footer-text)}
.copyright{position:absolute;top:65px;width:100%;text-align:center;font-size:8px;color:#6d6f84}
</style>
</head>
<body>
<header class="site-header">
  <div class="brand">Harborview Walk-In &amp; Family Care</div>
  <nav class="main-nav">
    <a class="active" href="#">HOME</a>
    <a href="#">SERVICES</a>
    <a href="#">PAYMENT &amp; INSURANCE</a>
    <a href="#">MEET OUR PROVIDERS</a>
  </nav>
  <a class="nav-cta" href="#"><strong>NEW PATIENTS</strong><span>ACCESS YOUR MEDICAL RECORDS</span></a>
</header>

<section class="hero">
  <div class="hero-photo" role="img" aria-label="Photo of the clinic reception area with a glass front desk and blue tiled wall"></div>
  <h1 class="hero-title">HIGHQUALITY</h1>
  <p class="hero-sub">COMPASSIONATE&nbsp; HEALTH CARE</p>
  <a class="hero-btn" href="#"><strong>NEW PATIENTS</strong><span>ACCESS YOUR MEDICAL RECORDS</span></a>
</section>

<h2 class="section-title">URGENT CARE &amp; FAMILY PRACTICE</h2>

<div class="about">
  <p class="intro">Harborview Walk-In &amp; Family Care is a family practice and urgent care clinic dedicated to providing high quality, compassionate health care, to patients of all ages.</p>
  <h3 class="hours-title">HOURS OF OPERATION</h3>
  <ul class="hours">
    <li>Monday-Friday 9am-6:30pm</li>
    <li>Saturday: CLOSED</li>
    <li>Sunday:&nbsp; CLOSED</li>
  </ul>
</div>

<div class="photo framed p1" role="img" aria-label="Photo of a staff member at work"></div>
<div class="photo p2" role="img" aria-label="Photo of the clinic front desk and cabinets"></div>
<div class="photo p3" role="img" aria-label="Group photo of the clinic staff"></div>
<div class="photo framed p4" role="img" aria-label="Photo of a nurse reaching for supplies"></div>
<div class="photo framed p5" role="img" aria-label="Photo of wooden clinic cabinets"></div>
<div class="chip"></div>

<div class="notice notice-a"><h3>Primary Care</h3><p>visits will be by appointment only.</p></div>
<div class="notice notice-b">We will accept our last new patient at 6:00p and our last established patient at 6:30p.</div>
<div class="notice notice-c">We will no longer be doing<br><span>DOT Physicals.</span></div>

<p class="privacy">Harborview Walk-In &amp; Family Care understands that information about your health is private and we know how important it is to keep your medical information protected. We follow all HIPAA guidelines to protect the privacy of your medical records. The privacy act below explains our privacy practices and how we may use and disclose your medical information. If you would like for Harborview Walk-In &amp; Family Care to release any or all of your medical information to others, you can make the request by signing a release and bring it with you at your next visit. If you would like to contact someone about the privacy and/or use of your medical information, you may contact us at 205-381-7260.</p>

<ul class="doc-links">
  <li><svg width="5" height="8" viewBox="0 0 5 8"><path d="M1 1l3 3-3 3" fill="none" stroke="#3a3c4d" stroke-width="1.2"/></svg><a href="#">Click here for HIPAA document.</a></li>
  <li><svg width="5" height="8" viewBox="0 0 5 8"><path d="M1 1l3 3-3 3" fill="none" stroke="#3a3c4d" stroke-width="1.2"/></svg><a href="#">Click here for Medical Release form.</a></li>
</ul>

<footer class="site-footer">
  <div class="footer-brand">Harborview Walk-In &amp; Family Care</div>
  <ul class="footer-col" style="left:337px"><li><a href="#">Home</a></li><li><a href="#">Services</a></li></ul>
  <ul class="footer-col" style="left:395px"><li><a href="#">Payment &amp; Insurance</a></li><li><a href="#">Meet Our Providers</a></li></ul>
  <ul class="footer-col" style="left:568px"><li>2218 Larkspur Mill Road</li><li>Suite 204</li><li>Coldbrook, AL 35290</li></ul>
  <ul class="footer-col" style="left:704px"><li>Phone: 205.381.7260</li><li>Fax: 205.381.7261</li><li>Email: info@harborviewcare.com</li></ul>
  <p class="copyright">Copyright ©2018 Harborview Walk-In and Family Care. All rights reserved.</p>
</footer>
</body>
</html>
```